need a Flyer for Plush Toy company

Need a Flyer for Plush Toy company ,

I upload a file for TEXT

Target Market(s)

Toys wholesalers , Supermarket

Industry/Entity Type

Toy Store

Colors
000000
ec1f27
c4c4c4

Requirements
Must have
• I have up loaded 3 files
• 1. Logo Registered Brand
• 2. customer's design in drawing
• 3. our ready samples based on Design
Nice to have
• happy kids in Nature ,
• happy kids in Ski ,
• different color Kids ,
• Multi culture concept

```html
<!DOCTYPE html>
<html lang="en">
<head>
<meta charset="utf-8">
<title>Tumo Pako – Plush Toy Flyer</title>
<link href="https://fonts.googleapis.com/css2?family=Gochi+Hand&family=Source+Sans+3:ital,wght@0,400;0,600;0,700;0,900;1,400&display=swap" rel="stylesheet">
<style>
  :root {
    --red: #c8120f;
    --red-bright: #ec1f27;
    --ink: #2b2b2b;
    --grey: #c4c4c4;
    --text: #444;
    --white: #ffffff;
    --stage: #ece8e3;
  }
  * { box-sizing: border-box; margin: 0; padding: 0; }
  html, body {
    width: 1200px; height: 943px; overflow: hidden;
    background: var(--stage);
    font-family: "Source Sans 3", Arial, sans-serif;
  }
  .flyer {
    position: absolute; left: 282px; top: 20px;
    width: 636px; height: 903px;
    background: var(--red);
    overflow: hidden;
  }
  .sheet {
    position: absolute; left: 26px; right: 26px; top: 26px; bottom: 0;
    background: var(--white);
  }
  .centered { position: absolute; left: 0; right: 0; text-align: center; }
  .tagline {
    top: 104px; font-family: "Gochi Hand", cursive, sans-serif;
    font-size: 26px; color: var(--red-bright);
  }
  .brand {
    top: 136px; display: flex; justify-content: center; align-items: center; gap: 14px;
  }
  .brand-dot { width: 26px; height: 26px; border-radius: 50%; background: var(--red); }
  .brand-name {
    font-size: 80px; font-weight: 900; color: var(--red); line-height: 1;
    letter-spacing: 1px;
  }
  .entity {
    top: 232px; font-size: 27px; font-style: italic; color: var(--ink);
  }
  .roles {
    top: 274px; font-size: 16px; font-weight: 700; color: var(--red-bright); line-height: 1.2;
  }
  .samples {
    position: absolute; top: 322px; left: 120px; width: 350px; height: 142px;
    border-radius: 60px;
    background: linear-gradient(90deg, #f4b6c9 0%, #f1f1ee 25%, #f19a3e 40%, #b8a7de 58%, #8fb3e0 75%, #f5d437 100%);
  }
  .about {
    position: absolute; top: 474px; left: 40px; right: 40px;
    font-size: 11.5px; color: var(--text); line-height: 1.35;
  }
  .about p { margin-bottom: 5px; }
  .about p:first-child { text-align: center; }
  .address {
    top: 588px; font-size: 15px; font-weight: 700; color: var(--ink);
  }
  .info {
    position: absolute; top: 616px; left: 40px; right: 40px;
    display: flex; justify-content: space-between;
    font-size: 11.5px; color: var(--ink); line-height: 1.35;
  }
  .info strong { font-weight: 700; }
  .contact { text-align: left; }
  .illustration {
    position: absolute; top: 726px; left: 150px; width: 336px; height: 92px;
    border-radius: 14px;
    background: linear-gradient(180deg, #f3e6d6 0%, #b7d9a3 45%, #a9cf93 100%);
  }
  .grass {
    position: absolute; left: 0; right: 0; bottom: 0; height: 130px;
  }
  .ribbon {
    position: absolute; left: 50%; top: 804px; transform: translateX(-50%) rotate(3deg);
    background: var(--red-bright); color: var(--white);
    font-size: 15px; font-weight: 700; padding: 6px 14px; white-space: nowrap;
  }
  .phone {
    top: 856px; color: var(--white); font-size: 14px; font-weight: 600;
    display: flex; justify-content: center; align-items: center; gap: 6px;
  }
</style>
</head>
<body>
  <div class="flyer">
    <div class="sheet">
      <div class="centered tagline">Have you been there?</div>
      <div class="centered brand">
        <span class="brand-dot"></span>
        <span class="brand-name">Tumo Pako</span>
      </div>
      <div class="centered entity">Einzelunternehmen / Family business</div>
      <div class="centered roles">Innovative Developer for Plush Toys<br>International Trader for Toys</div>
      <div class="samples" role="img" aria-label="Photo of six sample plush toys: pink rabbit, white bird, orange lion, purple elephant, blue bird and yellow chick"></div>
      <div class="about">
        <p>We live and work in Feldheim near to Rivertown Germany. We speak German and English.</p>
        <p>The toys are made in China, we are small family business, but we are professional in Plush toys business, right now we have successfully launched Projects with a huge Japanese 100 Yen Chain Store. Here in Flyer we show a Sample project.</p>
        <p>100 Yen = 0.90 USD , Our products can meet strictest Quality Control , but are with extremely Low Price to fit for Japanese Dollar Shop as well as his overseas Store around the world.</p>
      </div>
      <div class="centered address">Lindenweg 8, 50999 Feldheim Germany</div>
      <div class="info">
        <div class="bank">
          <strong>Bank information</strong><br>
          <strong>Kontoinhaber/Account Holder :</strong> Lena Moritz<br>
          <strong>IBAN :</strong> DE00 1234 5678 9012 3456 78<br>
          <strong>BIC :</strong> SMPLDEFF000
        </div>
        <div class="contact">
          <strong>hello@tumopako.example</strong><br>
          <strong>Fon</strong> +49 (0) 2200- 555 0100<br>
          <strong>Fax</strong> +49 (0) 2200- 555 0199<br>
          <strong>Ust-IdNr./VAT No.</strong> DE000111222
        </div>
      </div>
    </div>
    <svg class="grass" viewBox="0 0 636 130" preserveAspectRatio="none" role="img" aria-label="Green grass meadow along the bottom edge">
      <defs>
        <linearGradient id="meadow" x1="0" y1="0" x2="0" y2="1">
          <stop offset="0" stop-color="#6cb83a"/>
          <stop offset="1" stop-color="#3f8a24"/>
        </linearGradient>
      </defs>
      <path d="M0 40 Q160 10 318 30 T636 20 L636 130 L0 130 Z" fill="url(#meadow)"/>
    </svg>
    <div class="illustration" role="img" aria-label="Illustration of the six plush characters sitting on a green sofa"></div>
    <div class="ribbon">Happy kids in Nature | Happy kids in Ski</div>
    <div class="centered phone">
      <svg width="13" height="13" viewBox="0 0 24 24" aria-hidden="true"><path fill="#fff" d="M6.6 10.8a15.1 15.1 0 0 0 6.6 6.6l2.2-2.2a1 1 0 0 1 1-.25 11.4 11.4 0 0 0 3.6.57 1 1 0 0 1 1 1V20a1 1 0 0 1-1 1A17 17 0 0 1 3 4a1 1 0 0 1 1-1h3.5a1 1 0 0 1 1 1c0 1.25.2 2.45.57 3.570a1 1 0 0 1-.25 1z"/></svg>
      +49 (0) 170 5550 123
    </div>
  </div>
</body>
</html>
```